Web Design Project - Thornfield Analytics

I am a Mechanical Engineer running a one person consulting firm at this point. The hope is to expand in the future, but for now I simply need a website that conveys a professional appearance, and allows potential and existing clients to find me. Website design displaying contact information, CV for download, capabilities, past projects, etc. I've included four examples below from companies that provided the same service. I've only provided these as general reference for the type of work I do and how others have chosen to display this information. The design is completely at your discretion.

I've included the current Logo in the uploaded files section. I will provide content as requried.

http://www.quillmorept.com/
http://www.varlotex.com/
http://www.jupmarsystems.com/
http://dunsworthmachina.net/

Industry/Entity Type

Consulting

```html
<!DOCTYPE html>
<html lang="en">
<head>
<meta charset="utf-8">
<title>Thornfield Analytics</title>
<link href="https://fonts.googleapis.com/css2?family=Montserrat:wght@700&family=Nunito+Sans:ital,wght@0,400;0,600;0,800;1,400&family=Roboto:ital,wght@1,700;1,900&display=swap" rel="stylesheet">
<style>
:root{
  --ink:#3a3634;
  --text:#4a4644;
  --muted:#6b6765;
  --status:#7cb83c;
  --sidebar:#36312e;
  --accent:#f08a2c;
  --rule:#e4e4e4;
  --marker:#9a9896;
  --dot:#d6d6d6;
  --dot-on:#1a8fc0;
}
*{margin:0;padding:0;box-sizing:border-box}
html,body{width:1200px;height:781px;overflow:hidden;background:#fff}
body{position:relative;font-family:"Nunito Sans",sans-serif;color:var(--text)}
.hero{position:absolute;left:0;top:0;width:736px;height:262px;display:flex}
.hero-panel{height:100%}
.panel-gear{width:200px;background:linear-gradient(135deg,#1b2a3a 0%,#1a8fd8 45%,#2fb4ef 70%,#233040 100%)}
.panel-shaft{width:269px;background:linear-gradient(90deg,#202225 0%,#6f7378 35%,#1c1d20 55%,#9aa0a6 75%,#2b8fe0 100%);border-left:1px solid #fff}
.panel-cog{width:267px;background:linear-gradient(90deg,#f4f6f8 0%,#dfe8f0 45%,#5d7f98 70%,#2a3c4c 100%);border-left:1px solid #444}
.side-col{position:absolute;left:0;top:262px;width:200px;height:519px;border-right:1px solid var(--rule)}
.divider{position:absolute;left:0;top:602px;width:736px;border-top:1px solid var(--rule)}
.pager{position:absolute;top:275px;left:431px;display:flex;gap:8px}
.pager span{width:5px;height:5px;border-radius:50%;background:var(--dot)}
.pager span.on{background:var(--dot-on)}
h2{font-family:"Montserrat",sans-serif;font-weight:700;font-size:18px;line-height:22px;color:var(--ink);letter-spacing:-.2px}
.projects{position:absolute;left:233px;top:318px}
.projects ul{list-style:none;margin-top:17px}
.projects li{font-size:10.6px;height:19.2px;color:var(--ink);white-space:nowrap}
.projects .year{font-style:italic;color:var(--muted);margin:0 6px}
.projects .state{color:var(--status);font-weight:800;font-style:italic}
.contact{position:absolute;left:482px;top:318px}
.contact ul{list-style:none;margin-top:17px}
.contact li{font-size:10.6px;height:19.2px;color:var(--muted);padding-left:17px;position:relative;white-space:nowrap}
.contact li::before,.experience li::before{content:"";position:absolute;left:1px;top:3px;border-top:6px solid var(--marker);border-left:6px solid transparent}
.capabilities{position:absolute;left:233px;top:632px}
.capabilities .item{display:flex;margin-top:16px}
.capabilities .item:first-of-type{margin-top:22px}
.capabilities svg{flex:none;width:24px;height:24px;margin-right:13px;margin-top:0}
.capabilities p{font-size:10.6px;line-height:16px;color:var(--muted);width:428px}
.capabilities b{color:var(--ink);font-weight:800}
.sidebar{position:absolute;left:736px;top:0;width:464px;height:781px;background:var(--sidebar)}
.experience{position:absolute;left:29px;top:62px}
.experience h3{font-family:"Roboto",sans-serif;font-style:italic;font-weight:900;font-size:31.5px;line-height:38px;color:#fff;letter-spacing:.4px}
.experience ul{list-style:none;margin-top:2px}
.experience li{position:relative;padding-left:18px;height:19.2px;font-family:"Roboto",sans-serif;font-style:italic;font-weight:700;font-size:13px;color:var(--accent)}
.experience li::before{border-top-color:#8a8684}
</style>
</head>
<body>
<div class="hero">
  <div class="hero-panel panel-gear" role="img" aria-label="Close-up of a blue machined gear assembly"></div>
  <div class="hero-panel panel-shaft" role="img" aria-label="Polished steel shaft and bearing"></div>
  <div class="hero-panel panel-cog" role="img" aria-label="Steel cog teeth against a pale background"></div>
</div>
<div class="side-col"></div>
<div class="divider"></div>
<div class="pager"><span></span><span></span><span></span><span></span><span></span><span class="on"></span></div>

<section class="projects">
  <h2>PAST PROJECTS</h2>
  <ul>
    <li>Pump Housing<span class="year">(2012 - 2013)</span><span class="state">Done</span></li>
    <li>Valve Redesign<span class="year">(2012 - 2013)</span><span class="state">Done</span></li>
    <li>Conveyor Gearbox<span class="year">(2011 - 2012)</span><span class="state">Done</span></li>
    <li>Bridge Survey<span class="year">(2011 - 2012)</span><span class="state">Done</span></li>
    <li>Rotor Testing<span class="year">(2011 - 2012)</span><span class="state">Done</span></li>
    <li>Hydraulic Press<span class="year">(2010 - 2011)</span><span class="state">Done</span></li>
    <li>Turbine Mount<span class="year">(2010 - 2011)</span><span class="state">Done</span></li>
    <li>Drainage Plan<span class="year">(2010 - 2011)</span><span class="state">Done</span></li>
    <li>Crane Bracket<span class="year">(2009 - 2010)</span><span class="state">Done</span></li>
    <li>Site Leveling<span class="year">(2009 - 2010)</span><span class="state">Done</span></li>
    <li>Failure Study<span class="year">(2008 - 2009)</span><span class="state">Done</span></li>
  </ul>
</section>

<section class="contact">
  <h2>CONTACT</h2>
  <ul>
    <li>Thornfield Analytics</li>
    <li>Phone: (555) 014-2298</li>
    <li>info@thornfieldanalytics.com</li>
    <li>Download CV (PDF)</li>
    <li>Request a project quote</li>
  </ul>
</section>

<section class="capabilities">
  <h2>CAPABILITIES</h2>
  <div class="item">
    <svg viewBox="0 0 24 24" fill="none" stroke="#3a3634" stroke-width="1.4" stroke-linecap="round" aria-hidden="true">
      <circle cx="12" cy="12" r="3.2"/>
      <path d="M12 3v3M12 18v3M3 12h3M18 12h3M5.6 5.6l2.1 2.1M16.3 16.3l2.1 2.1M5.6 18.4l2.1-2.1M16.3 7.7l2.1-2.1"/>
    </svg>
    <p><b>Design &amp; Analysis:</b> Mechanical design, 3-D rendering and stress analysis of parts, forms and assemblies, from first sketch to shop-ready drawings.</p>
  </div>
  <div class="item">
    <svg viewBox="0 0 24 24" fill="none" stroke="#3a3634" stroke-width="1.4" stroke-linecap="round" aria-hidden="true">
      <path d="M4 19h16M6 19V9l6-4 6 4v10"/>
      <path d="M10 19v-5h4v5"/>
    </svg>
    <p><b>Consulting:</b> City and private consulting, site leveling and failure reviews. Clear reports, fair rates and direct access to the engineer on every project, large or small.</p>
  </div>
</section>

<aside class="sidebar">
  <nav class="experience">
    <h3>EXPERIENCE</h3>
    <ul>
      <li>3-D Rendering</li>
      <li>City Consulting</li>
      <li>Parts and Forms</li>
      <li>Leveling</li>
    </ul>
  </nav>
</aside>
</body>
</html>
```